Restaurant needs a vertical banner for fried catfish

Our restaurant is looking for an eye-catching 78.75in. x 36in. vertical physical banner ad for our fried catfish. Photos for the fried catfish will be provided as a reference but we will also accept anything similar to the photo. We will be using the following as our receptacle: https://www.plankoria.example/banner-stand/retractable-banner-stands/
The design must incorporate the following flavor texts:
Fried Catfish
Always Fresh!
Made from Scratch
Hand-cut Fillets
The Best Catfish in Texas
Served with fries, hush puppies, and a 32oz fountain drink
Also available by the pound!
The final design should be creative, professional, and eye-catching for customers.
Updates
Colors
Designer to choose colors to be used in the design.
Requirements
Must have
- We are open to any and all design elements, albeit the 'flavor texts' should not overpower, but complement the fried catfish photo. 'Fried Catfish' can be used in lieu of a main title/logo.
Nice to have
- Transparent or textured backgrounds that can encompass any or all part of the banner such as a cutting board, shadows, abstract, etc to show depth are a plus.
- Use of vectors or objects such as ribbons or shapes to encapsulate the 'flavor texts' are also encouraged.

```html
<!DOCTYPE html>
<html lang="en">
<head>
<meta charset="utf-8">
<title>Fried Catfish – Vertical Banner</title>
<link rel="stylesheet" href="https://fonts.googleapis.com/css2?family=Bebas+Neue&display=swap">
<style>
  :root {
    --banner-orange: #ef5a2a;
    --swirl-blue: #1ca9e6;
    --sun-yellow: #fcd418;
    --paper-white: #ffffff;
    --page-bg: #ffffff;
  }
  html, body {
    margin: 0;
    padding: 0;
    width: 1200px;
    height: 1200px;
    overflow: hidden;
    background: var(--page-bg);
  }
  .canvas {
    position: relative;
    width: 1200px;
    height: 1200px;
  }
  .banner {
    position: absolute;
    left: 331px;
    top: 17px;
    width: 520px;
    height: 1160px;
    display: block;
  }
  .banner-bg { fill: var(--banner-orange); }
  .brush-band-blue { fill: var(--swirl-blue); }
  .brush-band-yellow { fill: var(--sun-yellow); }
  .swirl-ring { fill: none; stroke: var(--swirl-blue); stroke-width: 40; }
  .sun-crescent { fill: var(--sun-yellow); }
  .catfish-illustration { fill: url(#catfish-tone); }
  .headline {
    font-family: "Bebas Neue", "Oswald", sans-serif;
    fill: var(--sun-yellow);
  }
  .offer-line {
    font-family: "Bebas Neue", "Oswald", sans-serif;
    fill: var(--paper-white);
    stroke: var(--paper-white);
    stroke-width: 1.2;
  }
</style>
</head>
<body>
<div class="canvas">
  <svg class="banner" viewBox="0 0 520 1160" xmlns="http://www.w3.org/2000/svg">
    <defs>
      <clipPath id="banner-clip">
        <rect width="520" height="1160"/>
      </clipPath>
      <radialGradient id="catfish-tone" cx="50%" cy="50%" r="55%">
        <stop offset="0%" stop-color="#ffffff" stop-opacity="0.85"/>
        <stop offset="55%" stop-color="#fde2d6" stop-opacity="0.7"/>
        <stop offset="100%" stop-color="#f7a07e" stop-opacity="0.6"/>
      </radialGradient>
    </defs>

    <rect class="banner-bg" width="520" height="1160"/>

    <g clip-path="url(#banner-clip)">
      <ellipse class="swirl-ring" cx="288" cy="551" rx="285" ry="345"/>

      <path class="brush-band-blue" d="M12 28 L505 24 L509 42 L500 54 L508 68 L14 72 L20 58 L10 46 Z"/>

      <path class="catfish-illustration" role="img"
            aria-label="White line illustration of a leaping catfish with whiskers, fins and a forked tail"
            d="M150 380 C230 360 300 420 330 500 C360 560 420 640 480 700 C440 760 360 790 300 900 C250 860 200 820 120 800 C60 760 20 650 40 560 C60 470 90 400 150 380 Z"/>

      <path class="sun-crescent" d="M350 440 C450 420 522 500 518 610 C516 700 470 770 400 805 C450 745 472 680 466 610 C460 520 420 470 350 440 Z"/>

      <path class="brush-band-yellow" d="M18 838 L498 835 L494 850 L499 866 L20 870 L26 854 Z"/>
    </g>

    <g class="headlines">
      <text class="headline" x="28" y="178" font-size="112" textLength="480" lengthAdjust="spacingAndGlyphs">FRIED CATFISH</text>
      <text class="headline" x="28" y="268" font-size="112" textLength="480" lengthAdjust="spacingAndGlyphs">ALWAYS FRESH</text>
      <text class="headline" x="28" y="333" font-size="66" textLength="482" lengthAdjust="spacingAndGlyphs">MADE FROM SCRATCH</text>
      <text class="headline" x="28" y="405" font-size="80" textLength="482" lengthAdjust="spacingAndGlyphs">HAND-CUT FILLETS</text>
    </g>

    <g class="offer">
      <text class="offer-line" x="28" y="945" font-size="62" textLength="484" lengthAdjust="spacingAndGlyphs">THE BEST CATFISH IN TEXAS</text>
      <text class="offer-line" x="28" y="1010" font-size="76" textLength="484" lengthAdjust="spacingAndGlyphs">SERVED WITH FRIES</text>
      <text class="offer-line" x="30" y="1068" font-size="54" textLength="478" lengthAdjust="spacingAndGlyphs">HUSH PUPPIES, AND A 32 OZ DRINK</text>
      <text class="offer-line" x="30" y="1118" font-size="54" textLength="478" lengthAdjust="spacingAndGlyphs">ALSO AVAILABLE BY THE POUND</text>
    </g>
  </svg>
</div>
</body>
</html>
```